Training Course Info Brochure

Hi there, I'm looking for a design for A4 Flyer (2-3 pages) on our new Course - Infection Control. I have included a previous brochure on our courses so the designed can see the look and feel we are looking for.

As this is about Infection Control, I would also like to see some RED in the design or wording.

The brochure will need to include quite a few industry/ government logos as well and graphics are important. I have included some (Health Care Industry workers) and am also open to other graphics.

Thanks for considering!

Target Market(s)

The Health profession and students wanting to work in the health field

Industry/Entity Type

Health Care

Font styles to use
Sans Serif

Colors
3277b5
f78f20
ffffff
ec1f27

Requirements
Must have
• Similar feel to the brochure I have included in this brief.

SOME RED lettering as we are teaching Infection Control during the COVID19 pandemic
Nice to have
• Lovely design with quite a few photos graphics

Company details:

Carrow Academy of Learning
RTO 73648
FREECALL : 1800 437 982
www.carrowlearning.edu.au
info@carrowlearning.edu.au

```html
<!DOCTYPE html>
<html lang="en">
<head>
<meta charset="utf-8">
<title>Infection Control Skill Set – Course Cost</title>
<link href="https://fonts.googleapis.com/css2?family=Comfortaa:wght@500;700&family=Ubuntu:wght@400;500;700&display=swap" rel="stylesheet">
<style>
  :root {
    --red: #d7181f;
    --ink: #3a3a3c;
    --rule: #3d3d3f;
    --navy: #2f4462;
    --gold: #c58a2a;
    --white: #ffffff;
  }
  * { margin: 0; padding: 0; box-sizing: border-box; }
  html, body { width: 849px; height: 1200px; overflow: hidden; background: var(--white); }
  .page { position: relative; width: 849px; height: 1200px; overflow: hidden; font-family: "Ubuntu", sans-serif; color: var(--ink); }

  .hero-photo {
    position: absolute; left: 0; top: 0; width: 849px; height: 530px;
    background: linear-gradient(100deg, #6f8fa8 0%, #b8c4cc 30%, #e2e0dc 55%, #ece9e4 75%, #dcd6cf 100%);
  }
  .virus-backdrop {
    position: absolute; left: 0; top: 527px; width: 849px; height: 615px;
    background: radial-gradient(ellipse at 20% 40%, #e0565a 0%, #b3222a 45%, #7a0f16 100%);
  }

  .info-card {
    position: absolute; left: 68px; top: 369px; width: 712px; height: 725px;
    background: var(--white);
    border-radius: 0 36px 0 52px;
  }

  .section-title {
    position: absolute; left: 127px;
    font-family: "Comfortaa", sans-serif; font-weight: 700;
    font-size: 44px; line-height: 1; color: var(--ink); letter-spacing: 0.5px;
  }
  .section-title .accent { color: var(--red); }
  .title-cost { top: 410px; }
  .title-about { top: 649px; }

  .section-rule { position: absolute; left: 127px; width: 594px; height: 5px; background: var(--rule); }
  .rule-cost { top: 461px; }
  .rule-about { top: 701px; }

  .unit-code { position: absolute; left: 131px; top: 484px; font-size: 12.5px; font-weight: 700; }

  .price-line {
    position: absolute; left: 131px; top: 522px; width: 600px;
    font-family: "Comfortaa", sans-serif; font-weight: 500; font-size: 21px; line-height: 28px; letter-spacing: 0.4px;
  }
  .price-line .free { font-family: "Ubuntu", sans-serif; font-weight: 400; color: var(--red); font-size: 34px; letter-spacing: 0; }

  .subsidy-note { position: absolute; left: 131px; top: 599px; font-size: 13px; }

  .about-lead { position: absolute; left: 127px; top: 723px; font-size: 15.5px; font-weight: 700; color: var(--red); }

  .about-body { position: absolute; left: 127px; top: 759px; width: 590px; font-size: 13.8px; line-height: 17px; }
  .about-body p { margin-bottom: 17px; }
  .about-body strong { font-weight: 700; }
  .about-body .highlight { color: var(--red); font-weight: 700; }

  .footer-band { position: absolute; left: 0; top: 1144px; width: 627px; height: 56px; background: var(--navy); }
  .footer-accent { position: absolute; left: 631px; top: 1144px; width: 218px; height: 56px; background: var(--gold); }
  .page-number {
    position: absolute; left: 50px; top: 1159px; width: 28px; height: 28px; border-radius: 50%;
    background: var(--white); border: 3px solid var(--gold);
    font-size: 13px; line-height: 22px; text-align: center; color: var(--ink);
  }
  .footer-url { position: absolute; left: 0; width: 685px; top: 1164px; text-align: center; font-size: 13.5px; color: var(--white); }
</style>
</head>
<body>
<div class="page">
  <div class="hero-photo" role="img" aria-label="Photo of a smiling carer in a white uniform gently holding the shoulder of an elderly woman in a blue blouse"></div>
  <div class="virus-backdrop" role="img" aria-label="Close-up red illustration of virus particles"></div>

  <div class="info-card"></div>

  <h2 class="section-title title-cost"><span class="accent">Course</span> Cost</h2>
  <div class="section-rule rule-cost"></div>
  <p class="unit-code">HLTINF001 - Comply with infection prevention and control policies and procedures.</p>
  <p class="price-line"><span class="free">FREE</span> infection control skill sets for everyone in Kestrel Territory or $325 for students outside of KT.</p>
  <p class="subsidy-note">Fully subsidised by the KT Government via the Skills Forward initiative.</p>

  <h2 class="section-title title-about"><span class="accent">About this</span> Course</h2>
  <div class="section-rule rule-about"></div>
  <p class="about-lead">Protect yourself and others in the community from infectious diseases.</p>
  <div class="about-body">
    <p>There is no better time than now, to formally Upskill yourself and your team with a Nationally Accredited unit of Competency in Infection Control prevention <strong>including the latest COVID19 infection control protocols</strong> (Kestrel Health Authority). Fast track your skills with Carrow’s Accredited Infection Control Skill set to get you job ready or enhance your current workplace skills.</p>
    <p>The COVID19 pandemic has highlighted the important of building the capacity and<br>understanding of the workforce to <span class="highlight">practice safe infection control procedures</span>.</p>
    <p>This skill set will provide you with the skills and knowledge to assist in protecting yourself and others in the community from infectious diseases.</p>
    <p>You will understand how infections are spread, ways of preventing the spread of infection and how to protect yourself and others from infection.</p>
    <p>The skill set is becoming increasingly important for all Health Care Workers – and all workers are encouraged to upskill themselves today, whether you are becoming Job Ready or for your professional development in Industry.</p>
  </div>

  <div class="footer-band"></div>
  <div class="footer-accent"></div>
  <div class="page-number">1</div>
  <p class="footer-url">www.carrowlearning.edu.au</p>
</div>
</body>
</html>
```